Maplebrook Youth Relief Trust

I need a site for a not for profit organization. The site requires an about us page, current projects, get involved and a contact us page
our not for profit will focus on three projects at a time the three focus would be childrens cancer, sick children and disadvantaged children
our logo is red and white so something that will complement this color scheme

Coding

Coded - Design and coding required

Number of Pages Required

5+ page

Font styles to use
Sans Serif

Colors
ec1f27
33a6d7
fbed22

Requirements
Must have
• an about us, contact us, current projects, home page, and
• get involved pages
• ability to update our pages easily

```html
<!DOCTYPE html>
<html lang="en">
<head>
<meta charset="utf-8">
<title>Maplebrook Youth Relief Trust</title>
<link rel="stylesheet" href="https://fonts.googleapis.com/css2?family=Noto+Serif:wght@400;700&display=swap">
<style>
:root{
  --red:#ec1f27;
  --blue:#33a6d7;
  --yellow:#fbed22;
  --navy:#1f6d8a;
  --ink:#555;
  --dark:#333;
  --grey:#ececec;
  --white:#fff;
  --serif:"Noto Serif", Georgia, serif;
}
*{box-sizing:border-box;margin:0;padding:0}
html,body{width:1200px;height:2871px;overflow:hidden}
body{position:relative;font-family:var(--serif);color:var(--ink);background:var(--white)}
section,header,footer{position:absolute;left:0;width:1200px}
.abs{position:absolute}
.photo{position:absolute}

/* hero */
.hero{top:0;height:655px;background:linear-gradient(120deg,#6b5a4c 0%,#8a7a63 40%,#5d6b5a 70%,#3e3a30 100%)}
.topbar{top:12px;left:144px;right:144px;height:20px;font-size:12px;color:var(--white);display:flex;justify-content:space-between;align-items:center}
.topbar .social{display:inline-flex;gap:6px;margin-left:6px;vertical-align:middle}
.topbar .social i{width:9px;height:9px;border-radius:50%;background:var(--white);display:inline-block}
.logo{top:38px;left:144px;width:149px;height:81px;background:var(--red);color:var(--white);display:flex;flex-direction:column;justify-content:center;align-items:center;text-align:center;font-size:16px;line-height:1.25;padding:0 8px}
.nav{top:38px;left:293px;width:762px;height:81px;background:rgba(31,109,138,.92);display:flex;align-items:center;padding-left:50px;gap:22px}
.nav a{color:var(--white);text-decoration:none;font-size:15px}
.nav .cta{margin-left:auto;margin-right:12px;background:var(--yellow);color:var(--dark);padding:9px 22px;font-size:14px}
.tagline{top:274px;left:722px;width:333px;height:287px;background:rgba(236,31,39,.93);color:var(--white);font-size:56px;line-height:59px;padding:48px 0 0 36px;letter-spacing:1px}
.tagline-bar{top:561px;left:736px;width:319px;height:11px;background:var(--yellow)}
.dots{top:622px;left:560px;display:flex;gap:8px}
.dots i{width:11px;height:11px;border-radius:50%;background:var(--white);display:block}
.dots i:first-child{background:var(--blue)}

/* welcome */
.welcome{top:655px;height:394px}
.welcome .photo{left:134px;top:67px;width:394px;height:262px;background:linear-gradient(135deg,#8a5a3a,#c99a5a 50%,#5b3a2a);box-shadow:0 12px 18px rgba(0,0,0,.45);border:4px solid var(--white)}
.welcome h1{left:568px;top:64px;font-weight:400;font-size:27px;line-height:38px;color:var(--blue)}
.welcome p{left:568px;top:170px;width:480px;font-size:17px;line-height:31px;color:#777}

/* focus */
.focus{top:1049px;height:494px;background:var(--red);color:var(--white)}
.focus h2{top:38px;width:100%;text-align:center;font-weight:400;font-size:27px}
.card{top:107px;width:287px}
.card .photo{position:relative;width:287px;height:172px;border:3px solid var(--white)}
.card h3{display:flex;align-items:center;gap:10px;font-weight:400;font-size:18px;margin-top:22px}
.card p{font-size:11px;line-height:18px;margin-top:10px}
.card .btn{display:inline-block;background:var(--white);color:var(--dark);font-size:12px;padding:7px 22px;margin-top:18px}

/* about */
.about{top:1543px;height:314px}
.about h2{left:144px;top:43px;font-weight:400;font-size:29px;color:var(--blue)}
.about .lead{left:144px;top:100px;width:430px;font-size:11px;line-height:20px;color:#555}
.about .motto{left:144px;top:210px;font-size:14px;color:#555}
.tile{top:34px;width:209px;height:215px;color:var(--white);padding:60px 20px 0;font-size:26px;line-height:31px}
.tile.vision{left:612px;background:var(--blue)}
.tile.objectives{left:846px;background:var(--yellow)}
.tile svg{display:block;margin-bottom:18px}

/* sick children */
.sick{top:1857px;height:363px;background:var(--grey)}
.sick .photo{left:147px;top:60px;width:242px;height:242px;border-radius:50%;background:radial-gradient(circle at 45% 40%,#d7a27a,#8b5a3c 70%);border:6px solid var(--white);box-shadow:0 4px 10px rgba(0,0,0,.3)}
.sick h2{left:419px;top:76px;font-weight:400;font-size:28px;color:var(--red)}
.sick p{left:419px;top:132px;width:640px;font-size:13px;line-height:25px;color:#444}

/* current projects */
.current{top:2220px;height:406px;background:#3b3b3b}
.current .photo{left:144px;top:84px;width:363px;height:232px;background:linear-gradient(160deg,#ddd,#888 60%,#555);border:4px solid var(--white)}
.current h2{left:532px;top:92px;font-weight:400;font-size:28px;color:var(--white)}
.current h3{left:532px;top:146px;font-weight:400;font-size:22px;color:var(--blue)}
.current p{left:532px;top:190px;width:520px;font-size:17px;line-height:27px;color:var(--white)}
.arrow{top:197px}

/* footer */
.footer{top:2626px;height:197px;background:var(--white)}
.col{top:26px;width:220px;font-size:11px;line-height:24px;color:#444}
.col h4{font-size:13px;color:var(--red);margin-bottom:12px}
.col .social{display:flex;gap:10px;margin-top:6px}
.col .social i{width:10px;height:10px;border-radius:50%;background:var(--blue);display:block}
.copyright{top:2823px;height:48px;border-top:1px solid #ddd;text-align:center;font-size:11px;line-height:46px;color:#555}
</style>
</head>
<body>

<header class="hero">
  <div class="photo" role="img" aria-label="Photo of a young girl studying a large globe in a classroom" style="inset:0;background:inherit"></div>
  <div class="topbar abs">
    <span>Connect With Us <span class="social"><i></i><i></i><i></i><i></i></span></span>
    <span>☎ Phone number : 1 800 555-0142</span>
  </div>
  <div class="logo abs">Maplebrook Youth Relief Trust</div>
  <nav class="nav abs">
    <a href="#">Home Page</a>
    <a href="#">About Us</a>
    <a href="#">Current Projects</a>
    <a href="#">Project Sick Children</a>
    <a href="#">Contact Us</a>
    <a href="#" class="cta">Get Involved</a>
  </nav>
  <div class="tagline abs">NO CHILD<br>SHOULD<br>SUFFER</div>
  <div class="tagline-bar abs"></div>
  <div class="dots abs"><i></i><i></i><i></i><i></i></div>
</header>

<section class="welcome">
  <div class="photo" role="img" aria-label="Photo of a boy reading a book in a library"></div>
  <h1 class="abs">Welcome to<br>Maplebrook Youth Relief Trust</h1>
  <p class="abs">The Maplebrook Youth Relief Trust is the federally registered charity for sick and disadvantaged children in Canada. Our aim is simple – we are working to empower children throughout Canada as they deal with the consequences of serious illness and complex situations.</p>
</section>

<section class="focus">
  <h2 class="abs">We Focus On Three Key Areas</h2>
  <div class="card abs" style="left:144px">
    <div class="photo" role="img" aria-label="Photo of a doctor holding a stethoscope" style="background:linear-gradient(135deg,#bfe3f2,#fff 55%,#d9d9d9)"></div>
    <h3><svg width="24" height="22" viewBox="0 0 24 22"><path d="M12 21 2 11a5.5 5.5 0 0 1 10-7 5.5 5.5 0 0 1 10 7z" fill="#fff"/></svg>Health Care</h3>
    <p>Sed ut perspiciatis unde omnis iste natus error sit voluptatem accusantium doloremque laudantium, totam rem aperiam, eaque ipsa quae ab illo inventore</p>
    <span class="btn">Read More</span>
  </div>
  <div class="card abs" style="left:457px">
    <div class="photo" role="img" aria-label="Photo of fresh vegetables and fruit" style="background:linear-gradient(135deg,#f3f3f3,#e0493a 40%,#6aa84f 75%,#f3f3f3)"></div>
    <h3><svg width="24" height="22" viewBox="0 0 24 22"><path d="M3 20C3 8 10 3 22 2c-1 12-7 18-17 16M4 19 14 9" fill="#fff" stroke="#fff" stroke-width="1.5"/></svg>Nutrition</h3>
    <p>Sed ut perspiciatis unde omnis iste natus error sit voluptatem accusantium doloremque laudantium, totam rem aperiam, eaque ipsa quae ab illo inventore</p>
    <span class="btn">Read More</span>
  </div>
  <div class="card abs" style="left:768px">
    <div class="photo" role="img" aria-label="Photo of paper boats led by a blue one" style="background:linear-gradient(135deg,#fafafa,#dcdcdc 60%,#4aa0d0)"></div>
    <h3><svg width="24" height="22" viewBox="0 0 24 22"><path d="M1 10 23 1 18 21 11 14 9 20 8 12z" fill="#fff"/></svg>Leadership Development</h3>
    <p>Sed ut perspiciatis unde omnis iste natus error sit voluptatem accusantium doloremque laudantium, totam rem aperiam, eaque ipsa quae ab illo inventore</p>
    <span class="btn">Read More</span>
  </div>
</section>

<section class="about">
  <h2 class="abs">About Us</h2>
  <p class="lead abs">The Maplebrook Youth Relief Trust is a federally registered charity for sick and disadvantaged children in Canada. Our aim is simple – we are working to empower children throughout Canada as hey deal with the Consequences of serious illness and complex situations. We focus on three key areas. Health Care, Nutrition, and Leadership Development.</p>
  <p class="motto abs">We have adopted the idea of "No child should suffer" for our work.</p>
  <div class="tile vision abs">
    <svg width="40" height="26" viewBox="0 0 40 26"><path d="M2 13C10 2 30 2 38 13 30 24 10 24 2 13z" fill="none" stroke="#fff" stroke-width="3"/><circle cx="20" cy="13" r="6" fill="#fff"/></svg>
    Our<br>Vision
  </div>
  <div class="tile objectives abs">
    <svg width="34" height="32" viewBox="0 0 34 32"><rect x="2" y="13" width="7" height="17" fill="#fff"/><path d="M12 14 18 2c4 0 5 3 4 8h9c2 0 3 2 2 4l-3 14c-1 2-2 3-4 3H12z" fill="#fff"/></svg>
    Objectives
  </div>
</section>

<section class="sick">
  <div class="photo" role="img" aria-label="Photo of three smiling children together"></div>
  <h2 class="abs">Project Sick Children</h2>
  <p class="abs">We serve children and youth dealing with illness and disabilities (physical and mental) and health challengesCollectively, we can make a difference to help many of these children. It is very simple and your support will make a difference. We need your help, so do your part and help when you can Each year thousands of children and families from across Canada seek care from the Children's health professionals. Thanks to your donations, we can help support the hospital's needs for state-of-the-art equipment and innovative research</p>
</section>

<section class="current">
  <div class="photo" role="img" aria-label="Black and white photo of children playing outdoors"></div>
  <svg class="arrow abs" style="left:68px" width="14" height="24" viewBox="0 0 14 24"><path d="M12 2 2 12l10 10" fill="none" stroke="#fff" stroke-width="3"/></svg>
  <svg class="arrow abs" style="left:1118px" width="14" height="24" viewBox="0 0 14 24"><path d="M2 2l10 10L2 22" fill="none" stroke="#fff" stroke-width="3"/></svg>
  <h2 class="abs">Current Projects</h2>
  <h3 class="abs">Project Disadvantage Children awareness</h3>
  <p class="abs">Maplebrook Youth Relief Trust supports programs that and positive experiences for children throughout Canada who are living in refuge, economic hardship or with other acute disadvantages. Some Programs we support include</p>
</section>

<footer class="footer">
  <div class="col abs" style="left:144px"><h4>Quick Links</h4>Home Page<br>About Us<br>Current Projects<br>Project Sick Children<br>Contact Us</div>
  <div class="col abs" style="left:377px"><h4>Other Links</h4>Terms Of Conditions<br>Privacy Policy</div>
  <div class="col abs" style="left:611px"><h4>Contact Us</h4>Address 220 Alderwood Ave ,<br>Kingsford,Ontario K0X 2B4<br><span style="display:block;margin-top:10px">Phone number : 1 800 555-0142</span></div>
  <div class="col abs" style="left:846px"><h4>Connect With Us</h4><div class="social"><i></i><i></i><i></i></div></div>
</footer>
<div class="copyright abs" style="left:0;width:1200px">© 2016 Company Name &nbsp;| All Rights Reserved</div>

</body>
</html>
```